Healthcare IT company looking for business card design

We develop IT systems for healthcare that significantly reduces cost and improves quality.

We want a business card design that is professional and clean, and using the colors in our logo.

Target Market(s)

Doctors and decision makers in the healthcare industry

Industry/Entity Type

Healthcare

Contact Information for Business Card

It should include
Name and title, address, telephone

Tobias Vrenholt, CEO
+46 712 418257
tobias@kelvaro.se

Font styles to use
Serif

Colors
0355a3
ed282f

Requirements
Must have
• Clean design
• Professional feel
Nice to have
• N/A
Should not have
• N/A

```html
<!DOCTYPE html>
<html lang="en">
<head>
<meta charset="utf-8">
<title>Kelvaro – Business Card</title>
<link rel="stylesheet" href="https://fonts.googleapis.com/css2?family=Source+Sans+3:wght@400;600;700&display=swap">
<style>
  :root {
    --brand-blue: #1560ae;
    --brand-red: #e5212b;
    --ink: #111111;
    --muted: #555555;
    --photo-grey: #bcbdc1;
    --paper: #ffffff;
    --backdrop: #e9e6e1;
  }
  * { margin: 0; padding: 0; box-sizing: border-box; }
  html, body { width: 1200px; height: 1200px; overflow: hidden; }
  body {
    background: var(--backdrop);
    font-family: "Source Sans 3", "Source Sans Pro", sans-serif;
    position: relative;
  }
  .card {
    position: absolute;
    left: 185px;
    width: 830px;
    height: 544px;
    border-radius: 30px;
    overflow: hidden;
  }
  .card--front { top: 48px; background: var(--paper); }
  .card--back { top: 608px; background: var(--brand-blue); }

  .front__band {
    position: absolute; left: 0; top: 0;
    width: 100%; height: 182px;
    background: var(--brand-blue);
  }
  .wordmark {
    position: absolute;
    color: var(--paper);
    font-weight: 600;
    letter-spacing: -1px;
    line-height: 1;
  }
  .front__wordmark { left: 40px; top: 34px; font-size: 104px; }
  .back__wordmark {
    left: 0; width: 100%; top: 190px;
    text-align: center; font-size: 160px;
  }

  .photo-frame {
    position: absolute; left: 572px; top: 42px;
    width: 217px; height: 216px;
    background: var(--paper);
    border-radius: 6px;
    padding: 9px;
  }
  .photo-slot {
    width: 100%; height: 100%;
    background: var(--photo-grey);
    border-radius: 6px;
    display: flex; align-items: center; justify-content: center;
    color: var(--paper);
    font-size: 27px;
  }

  .person { position: absolute; left: 44px; top: 220px; }
  .person__name { font-size: 40px; font-weight: 600; color: var(--ink); line-height: 1.1; }
  .person__title { font-size: 24px; font-weight: 600; color: var(--muted); margin-top: 2px; letter-spacing: 0.5px; }

  .contact { position: absolute; display: flex; align-items: center; color: var(--ink); }
  .contact__icon {
    width: 54px; height: 54px; border-radius: 50%;
    background: var(--brand-red);
    display: flex; align-items: center; justify-content: center;
    flex: none;
  }
  .contact__icon svg { width: 32px; height: 32px; }
  .contact__text { margin-left: 19px; white-space: nowrap; }
  .contact__text--large { font-size: 32px; }
  .contact__text--small { font-size: 26px; }
  .contact__text strong { font-weight: 700; }
</style>
</head>
<body>

<section class="card card--front">
  <div class="front__band"></div>
  <div class="wordmark front__wordmark">Kelvaro</div>

  <div class="photo-frame">
    <div class="photo-slot" role="img" aria-label="Portrait photo of the card holder">Photo Here</div>
  </div>

  <div class="person">
    <div class="person__name">Tobias Vrenholt</div>
    <div class="person__title">CEO</div>
  </div>

  <div class="contact" style="left:43px; top:328px;">
    <span class="contact__icon">
      <svg viewBox="0 0 24 24"><path fill="#fff" d="M6.6 2.5c.6-.3 1.3 0 1.6.6l1.6 3.4c.3.6.1 1.2-.4 1.6L8 9c.8 2.6 2.5 5 4.6 6.6l1.3-1.2c.5-.4 1.2-.5 1.7-.1l3.1 2.1c.5.4.7 1.1.4 1.7l-1 1.8c-.5.9-1.6 1.3-2.6 1C9.7 19 5.3 13.2 4.5 6.8c-.1-1 .4-2 1.3-2.5z"/></svg>
    </span>
    <span class="contact__text contact__text--large">+46 712 418257</span>
  </div>

  <div class="contact" style="left:376px; top:328px;">
    <span class="contact__icon">
      <svg viewBox="0 0 24 24"><rect x="6.5" y="2.5" width="11" height="19" rx="2" fill="none" stroke="#fff" stroke-width="2"/><rect x="8.5" y="5" width="7" height="11" fill="#fff"/><circle cx="12" cy="18.6" r="1" fill="#fff"/></svg>
    </span>
    <span class="contact__text contact__text--large">+46 712 418257</span>
  </div>

  <div class="contact" style="left:43px; top:391px;">
    <span class="contact__icon">
      <svg viewBox="0 0 24 24"><rect x="3" y="6" width="18" height="12" fill="none" stroke="#fff" stroke-width="1.8"/><path d="M3 6l9 7 9-7M3 18l7-6M21 18l-7-6" fill="none" stroke="#fff" stroke-width="1.8"/></svg>
    </span>
    <span class="contact__text contact__text--small">tobias@kelvaro.se</span>
  </div>

  <div class="contact" style="left:376px; top:391px;">
    <span class="contact__icon">
      <svg viewBox="0 0 24 24" fill="none" stroke="#fff" stroke-width="1.5"><circle cx="12" cy="12" r="9"/><ellipse cx="12" cy="12" rx="4" ry="9"/><path d="M3 12h18M4.5 7.5h15M4.5 16.5h15M12 3v18"/></svg>
    </span>
    <span class="contact__text contact__text--small">www.<strong>kelvaro</strong>.se</span>
  </div>

  <div class="contact" style="left:43px; top:453px;">
    <span class="contact__icon">
      <svg viewBox="0 0 24 24" fill="none" stroke="#fff" stroke-width="2" stroke-linejoin="round"><path d="M4 11l8-7 8 7v9H4z"/><path d="M9.5 20v-6h5v6"/></svg>
    </span>
    <span class="contact__text contact__text--small">Address, Street, City, State Zip</span>
  </div>
</section>

<section class="card card--back">
  <div class="wordmark back__wordmark">Kelvaro</div>
</section>

</body>
</html>
```